Step Boldly Toward Gain Promotional Flyer

I Need a one page, one-sided 8.5 x 11 editable promotional flyer that POPS!, designed in photoshop

[TITLE]Step Boldly Toward Gain: 3 BOLD Moves to Up-Level Your Business Now!

[CONTENT for the Flyer:]

At this content-rich event you will learn how to:
• Get out of feast and famine mode and into six, multi-six and/or seven figure-income mode
• Leapfrog your competition and become the obvious choice in your market
• Have your business aligned with who you are and what you want
• Enjoy your business far more than you imagined possible.
• Have more fun and time to yourself
• Live free and unbound!

Accolades
“Delphine helped us increase our six figure income by 41%...I feel reborn!” Marlene & Otis Pruitt, Vienna, VA

“…Delphine is a joy to listen to - compelling, smart, provocative…” – Dennis Ashcombe, Charlotte, North Carolina

“Delphine helped me increase my business by 66%...without me spending more time, money, or making cold calls! …I am in the zone!” Tina Worsley, Baltimore, MD
“Delphine is an energetic and dynamic speaker…content-rich…holds your attention to the very end!” Neil Barrow, Frmr Pres., Crane & Whitby, MD, MD, D.C., PA, DE, NJ
“Delphine is the real estate whisperer!” Hal Drummond, Washington D.C.

“Delphine was prepared, funny, informative and made a connection with each of our agents…Fabulous!…even my admins were PUMPED!!! – Paul Venable, New York

About Delphine:
Delphine is a highly regarded business development speaker & coach who knows how to pump up an audience and have them making more money, in less time, AND having more fun doing it! What’s not to love?! Consistently rated as an exceptional speaker and conference favorite! Among her work: Standout Method: How to Draw Your Best Buyers Time after Time!, Contact Sourcing Done Easy, The Worst Outreach Errors Real Estate Agents Commit and How to Steer Clear of Them, Slow Seasons Build Sharp Sellers, Drive Within the Head for Real Estate Agents.

[Also need a section for:]
Date: December 9, 2015, Time: 9:00 Am - 12:00 Noon, Place: Harbor Lantern Convention, Green Castle, PA

Target Market(s)

Real Estate Agents

Industry/Entity Type

Real Estate Agent

Font styles to use
Sans Serif

Colors
0655a3
f37122

Requirements
Must have
• the peak tier realty mentor logo
Nice to have
• step boldly toward gain logo; lots of POP! :-) ; open to other colors, accent colors.

```html
<!DOCTYPE html>
<html lang="en">
<head>
<meta charset="utf-8">
<title>Step Boldly Toward Gain – Event Flyer</title>
<link rel="stylesheet" href="https://fonts.googleapis.com/css2?family=Montserrat:wght@500;700;800&family=Roboto:wght@400;500;700&display=swap">
<style>
  :root {
    --navy: #1c2160;
    --blue: #0655a3;
    --orange: #f37122;
    --sky-top: #4f86c6;
    --sky-low: #d9e6f3;
    --suit: #1f2a4e;
    --ink: #333;
    --paper: #ffffff;
    --stage: #e7e7e7;
    --red: #d6283f;
  }
  * { box-sizing: border-box; margin: 0; padding: 0; }
  html, body { width: 1200px; height: 923px; overflow: hidden; background: var(--stage); }
  body { font-family: "Roboto", Arial, sans-serif; color: var(--ink); }

  .flyer {
    position: absolute; left: 260px; top: 21px;
    width: 680px; height: 880px; background: var(--paper);
    overflow: hidden; box-shadow: 0 6px 18px rgba(0,0,0,.18);
  }

  .hero {
    position: absolute; inset: 0 0 auto 0; height: 300px;
    background: linear-gradient(180deg, var(--sky-top) 0%, #8fb3dc 55%, var(--sky-low) 100%);
  }
  .hero-photo {
    position: absolute; right: 50px; top: 0; width: 270px; height: 300px;
    background: linear-gradient(180deg, #c3d3e6 0%, #6f86ad 22%, var(--suit) 48%, #151b36 100%);
  }
  .brand {
    position: absolute; left: 34px; top: 34px;
    font-family: "Montserrat", Arial, sans-serif; font-weight: 700; font-size: 19px;
    color: var(--navy); display: flex; align-items: center; gap: 8px;
  }
  .brand-dot { width: 12px; height: 12px; border-radius: 50%; background: var(--orange); }

  .headline {
    position: absolute; left: 0; top: 92px; width: 350px; height: 120px;
    background: var(--orange); padding: 16px 20px 0 44px;
    font-family: "Montserrat", Arial, sans-serif; font-weight: 800; font-size: 25px;
    line-height: 1.12; color: #fff; text-transform: uppercase;
  }
  .event-when { position: absolute; left: 44px; top: 226px; color: var(--navy); }
  .event-date { font-family: "Montserrat", Arial, sans-serif; font-weight: 800; font-size: 23px; }
  .event-date sup { font-size: 12px; }
  .event-time, .event-place { font-size: 14px; line-height: 1.4; font-weight: 500; }

  .stripe { position: absolute; right: 0; top: 246px; }

  .learn-bar {
    position: absolute; left: 0; top: 310px; width: 100%; height: 34px;
    background: var(--navy); color: #fff; padding: 8px 0 0 44px;
    font-family: "Montserrat", Arial, sans-serif; font-weight: 700; font-size: 15px;
  }
  .learn {
    position: absolute; left: 0; top: 344px; width: 100%; height: 170px;
    background: var(--orange); padding: 12px 0 0 44px;
  }
  .learn-list { list-style: none; }
  .learn-list li {
    color: #fff; font-size: 13px; line-height: 23px; display: flex; align-items: center; gap: 10px;
  }
  .learn-art {
    position: absolute; right: 40px; top: -84px; width: 120px; height: 90px;
    background: linear-gradient(160deg, #e0344b 0%, var(--red) 60%, #b81d34 100%);
  }

  .profile { position: absolute; left: 0; top: 514px; width: 100%; height: 316px; }
  .coach-photo {
    position: absolute; left: 200px; top: 20px; width: 140px; height: 130px;
    background: linear-gradient(160deg, #e9e4de 0%, #c9b9a7 60%, #2b2b33 100%);
  }
  .coach-name {
    position: absolute; left: 44px; top: 62px;
    font-family: "Montserrat", Arial, sans-serif; font-weight: 800; font-size: 14px; color: #111;
  }
  .coach-mark {
    position: absolute; left: 44px; top: 84px; width: 150px;
    font-family: "Montserrat", Arial, sans-serif; font-weight: 800; font-size: 15px;
    line-height: 1.15; color: var(--orange); text-transform: uppercase;
  }
  .about { position: absolute; left: 44px; top: 160px; width: 296px; }
  .section-title {
    font-family: "Montserrat", Arial, sans-serif; font-weight: 800; font-size: 14px;
    color: var(--orange); text-transform: uppercase; margin-bottom: 4px;
  }
  .about p { font-size: 9.6px; line-height: 1.5; text-align: justify; }

  .accolades { position: absolute; left: 366px; top: 16px; width: 280px; }
  .quote { font-size: 9px; line-height: 1.35; padding: 4px 0 5px; border-bottom: 1px dotted #bbb; }
  .quote:last-child { border-bottom: 0; }
  .quote cite { display: block; font-style: normal; font-weight: 700; color: #111; }

  .footer {
    position: absolute; left: 0; bottom: 0; width: 100%; height: 50px;
    background: var(--navy); color: #fff; display: flex; align-items: center;
    justify-content: flex-end; gap: 10px; padding-right: 34px; font-size: 14px;
  }
  .footer strong { font-size: 15px; }
</style>
</head>
<body>
<main class="flyer">
  <header class="hero">
    <div class="hero-photo" role="img" aria-label="Businessman in a dark suit shading his eyes and looking into the distance against a bright sky"></div>
    <div class="brand"><span class="brand-dot"></span>Step Boldly Toward Gain</div>
    <h1 class="headline">3 Bold Moves to Up-Level Your Business Now!</h1>
    <svg class="stripe" width="420" height="64" viewBox="0 0 420 64" aria-hidden="true">
      <polygon points="60,10 420,0 420,14 60,24" fill="#1c2160"/>
      <polygon points="130,30 420,18 420,64 100,64" fill="#f37122"/>
    </svg>
    <div class="event-when">
      <div class="event-date">9<sup>TH</sup> DECEMBER 2015</div>
      <div class="event-time">9.00 AM - 12.00 PM</div>
      <div class="event-place">Harbor Lantern Convention, Green Castle, PA</div>
    </div>
  </header>

  <div class="learn-bar">At this content-rich event you will learn how to:</div>
  <section class="learn">
    <div class="learn-art" role="img" aria-label="Illustration of rising red steps with a growth line and a flag at the top"></div>
    <ul class="learn-list">
      <li><svg width="13" height="11" viewBox="0 0 13 11"><path d="M1 6l4 4 7-9" stroke="#fff" stroke-width="2.2" fill="none"/></svg>Get out of feast and famine mode and into six, multi-six and/or seven figure-income mode</li>
      <li><svg width="13" height="11" viewBox="0 0 13 11"><path d="M1 6l4 4 7-9" stroke="#fff" stroke-width="2.2" fill="none"/></svg>Leapfrog your competition and become the obvious choice in your market</li>
      <li><svg width="13" height="11" viewBox="0 0 13 11"><path d="M1 6l4 4 7-9" stroke="#fff" stroke-width="2.2" fill="none"/></svg>Have your business aligned with who you are and what you want</li>
      <li><svg width="13" height="11" viewBox="0 0 13 11"><path d="M1 6l4 4 7-9" stroke="#fff" stroke-width="2.2" fill="none"/></svg>Enjoy your business far more than you imagined possible.</li>
      <li><svg width="13" height="11" viewBox="0 0 13 11"><path d="M1 6l4 4 7-9" stroke="#fff" stroke-width="2.2" fill="none"/></svg>Have more fun and time to yourself</li>
      <li><svg width="13" height="11" viewBox="0 0 13 11"><path d="M1 6l4 4 7-9" stroke="#fff" stroke-width="2.2" fill="none"/></svg>Live free and unbound!</li>
    </ul>
  </section>

  <section class="profile">
    <div class="coach-photo" role="img" aria-label="Portrait of the speaker in a dark blazer"></div>
    <h2 class="coach-name">DELPHINE CARVER</h2>
    <div class="coach-mark">Peak Tier Realty Mentor</div>
    <div class="about">
      <h3 class="section-title">About Delphine:</h3>
      <p>Delphine is a highly regarded business development speaker &amp; coach who knows how to pump up an audience and have them making more money, in less time, AND having more fun doing it! What's not to love?! Consistently rated as an exceptional speaker and conference favorite! Among her work: Standout Method: How to Draw Your Best Buyers Time after Time!, Contact Sourcing Done Easy, The Worst Outreach Errors Real Estate Agents Commit and How to Steer Clear of Them, Slow Seasons Build Sharp Sellers, Drive Within the Head for Real Estate Agents.</p>
    </div>
    <div class="accolades">
      <h3 class="section-title">Accolades</h3>
      <blockquote class="quote">“Delphine helped us increase our six figure income by 41%...I feel reborn!”<cite>Marlene &amp; Otis Pruitt, Vienna, VA</cite></blockquote>
      <blockquote class="quote">“…Delphine is a joy to listen to - compelling, smart, provocative…”<cite>Dennis Ashcombe, Charlotte, North Carolina</cite></blockquote>
      <blockquote class="quote">“Delphine helped me increase my business by 66%...without me spending more time, money, or making cold calls! …I am in the zone!”<cite>Tina Worsley, Baltimore, MD</cite></blockquote>
      <blockquote class="quote">“Delphine is an energetic and dynamic speaker…content-rich…holds your attention to the very end!”<cite>Neil Barrow, Frmr Pres., Crane &amp; Whitby, MD, MD, D.C., PA, DE, NJ</cite></blockquote>
      <blockquote class="quote">“Delphine is the real estate whisperer!”<cite>Hal Drummond, Washington D.C.</cite></blockquote>
      <blockquote class="quote">“Delphine was prepared, funny, informative and made a connection with each of our agents…Fabulous!…even my admins were PUMPED!!!”<cite>Paul Venable, New York</cite></blockquote>
    </div>
  </section>

  <footer class="footer">
    <span>For more information, Call Us</span>
    <svg width="18" height="18" viewBox="0 0 24 24" aria-hidden="true"><circle cx="12" cy="12" r="11" fill="none" stroke="#fff" stroke-width="1.5"/><path d="M8 6c-1 1-1.5 2.5 0 5s3.5 5 6 6c1.5.5 2.5-.3 3-1l-2-2-1.5 1c-1.5-.8-3-2.5-3.5-3.5l1-1.5-2-2z" fill="#fff"/></svg>
    <strong>012 - 4820 317</strong>
  </footer>
</main>
</body>
</html>
```